Banner for my Adult Tube Site

Hi,
i need 5 animated banner .gif for my Adult Tube Site https://velvorinstream.example
N.2 300x250
N.2 728x90
N.1 160x600
You can add image in the banner only with  free copyright.
I leave you to think about something that attracts attention to being clicked.

```html
<!DOCTYPE html>
<html lang="en">
<head>
<meta charset="utf-8">
<title>Velvorin Stream – Leaderboard Banner</title>
<link href="https://fonts.googleapis.com/css2?family=Questrial&display=swap" rel="stylesheet">
<style>
  :root {
    --frame-pink: #f2477f;
    --frame-pink-light: #ff8fb4;
    --panel-dark: #141013;
    --panel-mid: #231a1f;
    --cta-white: #ffffff;
    --cta-glow: #ff4f8d;
    --spark: #e0306a;
    --photo-light: #e9d6cc;
    --photo-skin: #c9a18d;
    --photo-shadow: #3a2a27;
  }
  * { margin: 0; padding: 0; box-sizing: border-box; }
  html, body {
    width: 1200px;
    height: 148px;
    overflow: hidden;
    background: #ffffff;
  }
  .banner {
    position: relative;
    width: 1200px;
    height: 148px;
    background: var(--frame-pink);
    padding: 5px;
  }
  .banner__inner {
    position: relative;
    width: 100%;
    height: 100%;
    overflow: hidden;
    background: radial-gradient(ellipse at 40% 60%, var(--panel-mid) 0%, var(--panel-dark) 70%);
  }
  .banner__sparks {
    position: absolute;
    inset: 0;
    width: 100%;
    height: 100%;
  }
  .banner__cta {
    position: absolute;
    left: 250px;
    top: 74px;
    transform: translateY(-50%);
    font-family: "Questrial", "Century Gothic", sans-serif;
    font-size: 38px;
    letter-spacing: 1px;
    color: var(--cta-white);
    text-decoration: none;
    text-shadow: 0 0 4px var(--cta-glow), 0 0 10px var(--cta-glow), 0 0 18px rgba(255, 79, 141, 0.6);
  }
  .banner__photo {
    position: absolute;
    top: 0;
    right: 0;
    width: 600px;
    height: 100%;
    background:
      linear-gradient(90deg, rgba(20,16,19,1) 0%, rgba(255,143,180,0.55) 10%, rgba(255,255,255,0) 22%),
      linear-gradient(100deg, var(--photo-light) 20%, var(--photo-skin) 40%, var(--photo-shadow) 58%, var(--photo-skin) 72%, var(--photo-shadow) 86%, var(--photo-light) 100%);
  }
  .banner__photo-edge {
    position: absolute;
    top: 0;
    left: 0;
    width: 100%;
    height: 6px;
    background: linear-gradient(90deg, var(--frame-pink-light), rgba(255,143,180,0));
  }
</style>
</head>
<body>
  <div class="banner">
    <div class="banner__inner">
      <svg class="banner__sparks" viewBox="0 0 1190 138" aria-hidden="true">
        <circle cx="170" cy="88" r="1.6" fill="var(--spark)"/>
        <circle cx="320" cy="40" r="1.4" fill="var(--spark)"/>
        <circle cx="600" cy="72" r="1.6" fill="var(--spark)"/>
        <circle cx="560" cy="24" r="1.2" fill="var(--spark)"/>
        <circle cx="90" cy="30" r="1.2" fill="var(--spark)"/>
      </svg>
      <a class="banner__cta" href="https://velvorinstream.example">CLICK HERE</a>
      <div class="banner__photo" role="img" aria-label="Promotional photo area for the streaming site">
        <div class="banner__photo-edge"></div>
      </div>
    </div>
  </div>
</body>
</html>
```